Kavro Global Stationery & Logo Design

We are looking for a logo and stationary design for our business, which should include:
1) Letterhead
2) Business cards
3) A4 folders for company marketing materials
4) Envelops and
5) A4 file covers
We are international business consultants and tax advisers. We help companies with entering new markets by developing a market entry strategy, finding business partners and providing cross borders tax and finance advice.
We operate in the United Kingdom, Poland and India. Our target market includes middle and large companies from these three countries.
Company Name: Kavro Global Ltd.
Address: 12 Brackwell Row, Tanhurst, London, EC1V 4QT,
email: hello@kavroglobal.example
Website: www.kavroglobal.example
Phone: +44 (0) 20 3918 4462
Company Slogan: Clear Answers for a Busy Planet
Vision: To be the first choice for clients by delivering exceptional service through innovation and excellence
Mission: To persevere and achieve excellence in our endeavours through simplicity, respect and creativity
Values: Delivering Innovation with Creativity, Integrity, Achieving Excellence, Fun and Respect and Giving Back to Society.
Project Specification
Our preferred colour is royal blue however, we are open to ideas. We would like a design that is elegant but innovative, sleek and modern. The message we would like to convey is that we are professional and trustworthy business partners.
Please do not use Times New Roman or similar fonts.
Logo
The name of the company is Kavro Global Ltd and the logo can only include the company name although we would prefer to use only ‘Kavro Global’ without ‘Ltd’. Kavro does not need to be in capital letters.
Business Cards
Double sided business cards for our British, Polish and Indian office. The addresses should be as follows:
Kavro Global Ltd
12 Brackwell Row, Tanhurst, London, EC1V 4QT, email: name@kavroglobal.example, www.kavroglobal.example, +44 (0) 20 3918 4462
Kavro Global (Poland) sp. z o.o.
ul. Lipowska 38 lok. 214, 00-812 Warszawa, name@kavroglobal.example, www.kavroglobal.example
+48 (0) 22 415 6039
Kavro Global (India) Pvt. Ltd.
Trade Plaza, 29 Harimohan Lane, 3rd Floor, Kolkata, 700 046, name@kavroglobal.example, www.kavroglobal.example
+91 (0) 33 2871 9043
The names and email addresses will be confirmed once a winning design has been selected.
The business cards should include the company slogan and QR code.
Letterhead
All three addresses need to be on the letterhead. Email address should be hello@kavroglobal.example. Design of continuation sheets should be different to the front page.
A4 folders
We would like the outer and inside pages to have a slightly different design. The company slogan, vision, mission and the three offices’ addresses should also come somewhere on the folder. We do not want the design to include too many photos and would be happy with a design which does not have them at all but any other graphics are fine.
A4 file covers
We would need a front, back and side page. Company slogan and the three offices’ addresses should be included.
Envelopes
Window and regular DL and A4 envelopes.
Updates
Project Deadline Extended
Reason: The proposals we have received so far are not in line with our expectations so we would like to give the designer a bit more time to prepare a few new looks. Also, what we have received so far are only logos and the remaining items in our brief have not been prepared yet.

```html
<!DOCTYPE html>
<html lang="en">
<head>
<meta charset="utf-8">
<title>Kavro Global Letterhead</title>
<link href="https://fonts.googleapis.com/css2?family=Cormorant+Garamond:wght@400;500&family=Playfair+Display:wght@400&display=swap" rel="stylesheet">
<style>
  :root {
    --backdrop: #3b3652;
    --paper: #f2f1ef;
    --ink: #4a4a4e;
    --ink-soft: #909095;
    --brand: #3a3f8f;
  }
  * { margin: 0; padding: 0; box-sizing: border-box; }
  html, body { width: 1200px; height: 697px; overflow: hidden; }
  body {
    background: var(--backdrop);
    font-family: "Cormorant Garamond", Georgia, serif;
    color: var(--ink);
  }
  .letterhead {
    position: absolute;
    left: 374px; top: 28px;
    width: 452px; height: 640px;
    background: var(--paper);
    box-shadow: 0 10px 30px rgba(0,0,0,.35);
  }
  .brand {
    position: absolute; left: 34px; top: 58px;
    display: flex; flex-direction: column; align-items: flex-start; gap: 8px;
  }
  .brand-mark { width: 34px; height: 34px; background: var(--brand); }
  .brand-name { font-size: 15px; font-weight: 500; color: var(--brand); white-space: nowrap; }
  .slogan {
    position: absolute; left: 160px; top: 50px; width: 230px;
    font-family: "Playfair Display", Georgia, serif;
    font-weight: 400; font-size: 19px; line-height: 1.2; color: var(--ink);
  }
  .meta {
    position: absolute; left: 18px; top: 134px; width: 124px;
    text-align: right; font-size: 8px; line-height: 1.5; color: var(--ink-soft);
  }
  .meta-label {
    font-variant: small-caps; letter-spacing: .06em;
    color: var(--ink); font-size: 9px; font-weight: 500;
  }
  .meta-block { margin-bottom: 18px; }
  .body {
    position: absolute; left: 160px; top: 134px; width: 262px;
    font-size: 8.5px; line-height: 1.55; color: var(--ink-soft);
  }
  .body p { margin-bottom: 14px; }
  .signature { position: absolute; left: 160px; top: 440px; }
  .signature-name { font-variant: small-caps; font-size: 10px; font-weight: 500; color: var(--ink); letter-spacing: .05em; }
  .signature-role { font-variant: small-caps; font-size: 8px; color: var(--ink-soft); }
  .footer {
    position: absolute; left: 160px; top: 556px; width: 272px;
    font-size: 7px; line-height: 1.55; color: var(--ink-soft);
  }
  .footer-office { white-space: nowrap; }
  .footer-contact { margin-top: 3px; }
</style>
</head>
<body>
  <main class="letterhead">
    <div class="brand">
      <span class="brand-mark"></span>
      <span class="brand-name">Kavro Global</span>
    </div>
    <h1 class="slogan">Clear Answers for a Busy Planet</h1>

    <aside class="meta">
      <div class="meta-block">
        <div class="meta-label">Date</div>
        <div>05 . 15 . 2015</div>
      </div>
      <div class="meta-block">
        <div class="meta-label">Address</div>
        <div>12 Brackwell Row, Tanhurst,<br>London, EC1V 4QT,<br>City Name, Country Name</div>
      </div>
    </aside>

    <section class="body">
      <p>Kavro Global Ltd. consectetur adipiscing elit.</p>
      <p>We are international business consultants and tax advisers. We help companies with entering new markets by developing a market entry strategy, finding business partners and providing cross borders tax and finance advice.</p>
      <p>We operate in the United Kingdom, Poland and India. Our target market includes middle and large companies from these three countries.</p>
      <p>Vision: To be the first choice for clients by delivering exceptional service through innovation and excellence</p>
      <p>Mission: To persevere and achieve excellence in our endeavours through simplicity, respect and creativity</p>
      <p>Values: Delivering Innovation with Creativity, Integrity, Achieving Excellence, Fun and Respect and Giving Back to Society.</p>
    </section>

    <div class="signature">
      <div class="signature-name">Jon Ashby</div>
      <div class="signature-role">Corporative</div>
    </div>

    <footer class="footer">
      <div class="footer-office">London · 12 Brackwell Row, Tanhurst, London, EC1V 4QT · +44 (0) 20 3918 4462</div>
      <div class="footer-office">Warszawa · ul. Lipowska 38 lok. 214, 00-812 Warszawa · +48 (0) 22 415 6039</div>
      <div class="footer-office">Kolkata · Trade Plaza, 29 Harimohan Lane, 3rd Floor, Kolkata, 700 046</div>
      <div class="footer-office">+91 (0) 33 2871 9043</div>
      <div class="footer-contact">e hello@kavroglobal.example · w www.kavroglobal.example</div>
    </footer>
  </main>
</body>
</html>
```